Stationery Design Project

KT7 Staffing requires letterhead and business card designs for a company based in London. Just like the name, we're a management resourcing company, providing resources to third party companies. You can see www.kt7staffing-example.com for ideas on existing colour schemes and design concepts that have been implimented and agreed to. Ultimately the design should broadcast professionalism, safety and the concept of growth.

Target Market(s)

Financial institutes; friendly societies (All UK based)

Industry/Entity Type

Safety

Requirements
Must have
• Files produced should be print ready; and the text in them editable (eg address, name etc)

```html
<!DOCTYPE html>
<html lang="en">
<head>
<meta charset="utf-8">
<title>KT7 Staffing – Business Card</title>
<link rel="stylesheet" href="https://fonts.googleapis.com/css2?family=Roboto:wght@300;500&family=Tinos:ital@1&display=swap">
<style>
  :root {
    --card-bg: #eef3f3;
    --card-bg-edge: #e3eaea;
    --map-tone: #d9e1e1;
    --brand-teal: #33b39a;
    --rule-teal: #7fd3c9;
    --address-teal: #79cfc6;
    --name-blue: #4aa3ee;
    --title-teal: #3cc6ae;
    --skyline-light: #b9ecfb;
    --skyline-deep: #4fb6e6;
  }
  html, body {
    margin: 0;
    padding: 0;
    width: 1200px;
    height: 700px;
    overflow: hidden;
  }
  .card {
    position: relative;
    width: 1200px;
    height: 700px;
    overflow: hidden;
    background: radial-gradient(ellipse at 50% 45%, var(--card-bg) 0%, var(--card-bg) 55%, var(--card-bg-edge) 100%);
    font-family: "Roboto", Arial, sans-serif;
  }
  .world-map {
    position: absolute;
    left: 0;
    top: 0;
    width: 1200px;
    height: 700px;
    background:
      radial-gradient(ellipse 220px 160px at 230px 170px, var(--map-tone), transparent 70%),
      radial-gradient(ellipse 120px 200px at 430px 520px, var(--map-tone), transparent 70%),
      radial-gradient(ellipse 170px 230px at 650px 380px, var(--map-tone), transparent 70%),
      radial-gradient(ellipse 330px 170px at 850px 170px, var(--map-tone), transparent 70%),
      radial-gradient(ellipse 110px 80px at 1050px 560px, var(--map-tone), transparent 70%);
    opacity: 0.8;
  }
  .brand {
    position: absolute;
    left: 42px;
    top: 82px;
    display: flex;
    align-items: center;
    gap: 18px;
  }
  .brand-mark {
    width: 64px;
    height: 64px;
    border-radius: 50%;
    background: var(--brand-teal);
  }
  .brand-name {
    font-weight: 500;
    font-size: 52px;
    color: var(--brand-teal);
    letter-spacing: 1px;
  }
  .skyline {
    position: absolute;
    left: 962px;
    top: 54px;
    width: 162px;
    height: 116px;
    border-radius: 6px;
    background: linear-gradient(180deg, var(--skyline-light), var(--skyline-deep));
  }
  .contact-line {
    position: absolute;
    left: 66px;
    top: 180px;
    margin: 0;
    font-weight: 300;
    font-size: 20px;
    letter-spacing: 2.6px;
    color: var(--address-teal);
    white-space: nowrap;
  }
  .header-rule {
    position: absolute;
    left: 0;
    top: 216px;
    width: 1200px;
    height: 2px;
    background: var(--rule-teal);
  }
  .person-name,
  .person-title {
    position: absolute;
    left: 0;
    width: 1200px;
    margin: 0;
    text-align: center;
    font-family: "Tinos", "Times New Roman", serif;
    font-style: italic;
    font-weight: 400;
  }
  .person-name {
    top: 335px;
    font-size: 64px;
    color: var(--name-blue);
    word-spacing: 14px;
    text-shadow: 0 0 6px #ffffff;
  }
  .person-title {
    top: 460px;
    font-size: 62px;
    color: var(--title-teal);
    text-shadow: 0 0 6px #ffffff;
  }
</style>
</head>
<body>
  <main class="card">
    <div class="world-map" role="img" aria-label="Faint world map in light grey behind the card"></div>

    <div class="brand">
      <span class="brand-mark"></span>
      <span class="brand-name">KT7 Staffing</span>
    </div>

    <div class="skyline" role="img" aria-label="Blue three-dimensional city skyline illustration"></div>

    <p class="contact-line">18 Harrow Lane, London, UK&nbsp;(020) 555-0148</p>
    <div class="header-rule"></div>

    <h1 class="person-name">Daniel Marsh</h1>
    <p class="person-title">CEO</p>
  </main>
</body>
</html>
```